Family Owned Construction Company Needs Modern Business Cards

We need a new design for our business cards. We are a family owned construction company, Brantwell Construction, based in Mendon, Vermont and would like to add in our new logo and find a more modern look. We also want to use our old to make sure people know who we are. We do site development, highway, environmental, demolition, utility and aggregate.

Contact Information for Business Card

We want to have the office address, 418 Quarry Ridge Road, Harlow Springs, ME 04788 and our phone (802) 555-0137 and fax (802) 555-0164 on there as well. Our website is www.brantwellinc.example. There should be a place for the person's name, title, cell number, and email address on the card. Words that we would like to be associated with our company are honesty, predictable, reliable, integrity, dedicated, built right quality, consistent, whatever it takes, and innovation. Safety is also very important to us.

Font styles to use
Serif
Sans Serif
Other font styles liked:
• Square 721 Extented

Colors
0255a3
ffffff

Requirements
Must have
• Office address, phone number and fax number. New logo with excavator
Nice to have
• That we do site development, highway, environmental, demolition, utility, and aggregate. Both logos

```html
<!DOCTYPE html>
<html lang="en">
<head>
<meta charset="utf-8">
<title>Brantwell Construction – Business Cards</title>
<link href="https://fonts.googleapis.com/css2?family=Open+Sans:wght@400;600;700&display=swap" rel="stylesheet">
<style>
  :root {
    --brand-blue: #0255a3;
    --card-blue: #0a3fb8;
    --white: #ffffff;
    --ink: #1a1a1a;
    --faint: #e6e6e6;
    --backdrop: #e9e9e7;
  }
  * { box-sizing: border-box; margin: 0; padding: 0; }
  html, body { width: 1200px; height: 1021px; overflow: hidden; }
  body {
    background: var(--backdrop);
    font-family: "Open Sans", Arial, sans-serif;
    position: relative;
  }
  .card {
    position: absolute;
    left: 220px;
    width: 760px;
    height: 434px;
    box-shadow: 0 6px 18px rgba(0,0,0,.18);
    overflow: hidden;
  }
  .card--front { top: 52px; background: var(--white); }
  .card--back { top: 535px; background: var(--card-blue); color: var(--white); }

  /* Front */
  .wordmark {
    position: absolute; top: 40px; right: 44px;
    display: flex; align-items: center; gap: 12px;
    color: var(--brand-blue); font-weight: 700; font-size: 26px; letter-spacing: .5px;
  }
  .wordmark__square { width: 22px; height: 22px; background: var(--brand-blue); flex: none; }
  .faint-name {
    position: absolute; top: 150px; right: 50px;
    color: var(--faint); font-weight: 700; font-size: 40px; text-align: right; line-height: 1.15;
  }
  .identity {
    position: absolute; left: 42px; top: 150px;
    border-left: 10px solid var(--brand-blue); padding-left: 12px;
  }
  .identity__name { font-size: 26px; color: var(--ink); line-height: 1.1; }
  .identity__name strong { font-weight: 700; }
  .identity__title { font-size: 18px; color: var(--brand-blue); font-weight: 600; }
  .contact-list { position: absolute; left: 120px; top: 250px; list-style: none; }
  .contact-list li {
    display: flex; align-items: flex-start; gap: 16px;
    font-size: 17px; color: var(--ink); line-height: 1.35; margin-bottom: 3px;
  }
  .contact-list svg { width: 18px; height: 18px; flex: none; margin-top: 3px; fill: var(--brand-blue); }
  .website--front {
    position: absolute; right: 44px; bottom: 130px;
    color: var(--brand-blue); font-weight: 600; font-size: 17px;
  }

  /* Back */
  .wordmark--back {
    position: absolute; top: 130px; left: 0; right: 0;
    display: flex; justify-content: center; align-items: center; gap: 16px;
    color: var(--white); font-weight: 700; font-size: 40px; letter-spacing: .5px;
  }
  .wordmark--back .wordmark__square { width: 34px; height: 34px; background: var(--white); }
  .website--back {
    position: absolute; top: 205px; right: 110px;
    font-size: 17px;
  }
  .services {
    position: absolute; bottom: 46px; left: 20px; right: 20px; text-align: center;
    font-size: 16px; letter-spacing: .2px; white-space: nowrap;
  }
  .services span { margin: 0 6px; }
</style>
</head>
<body>
  <section class="card card--front" aria-label="Business card front">
    <div class="wordmark"><span class="wordmark__square"></span>Brantwell Construction Inc.</div>
    <div class="faint-name" aria-hidden="true">Brantwell<br>Construction Inc.</div>
    <div class="identity">
      <p class="identity__name">Your <strong>Name</strong></p>
      <p class="identity__title">Job Title</p>
    </div>
    <ul class="contact-list">
      <li><svg viewBox="0 0 24 24"><path d="M12 2a7 7 0 0 0-7 7c0 5 7 13 7 13s7-8 7-13a7 7 0 0 0-7-7zm0 9.5a2.5 2.5 0 1 1 0-5 2.5 2.5 0 0 1 0 5z"/></svg><span>418 Quarry Ridge Road<br>Harlow Springs, ME 04788</span></li>
      <li><svg viewBox="0 0 24 24"><path d="M7 1h10a2 2 0 0 1 2 2v18a2 2 0 0 1-2 2H7a2 2 0 0 1-2-2V3a2 2 0 0 1 2-2zm0 3v14h10V4H7zm5 15.5a1 1 0 1 0 0 2 1 1 0 0 0 0-2z"/></svg><span>000 000 0000</span></li>
      <li><svg viewBox="0 0 24 24"><path d="M3 8c0-2 4-4 9-4s9 2 9 4v2h-5V8H8v2H3V8zm4 4h10l3 6v3H4v-3l3-6zm5 2a2.5 2.5 0 1 0 0 5 2.5 2.5 0 0 0 0-5z"/></svg><span>(802) 555-0137</span></li>
      <li><svg viewBox="0 0 24 24"><path d="M7 2h10v6H7V2zM3 9h18v11H3V9zm3 3v2h4v-2H6zm8 0v2h4v-2h-4zm-8 4v2h12v-2H6z"/></svg><span>(802) 555-0164</span></li>
      <li><svg viewBox="0 0 24 24"><path d="M2 5h20v14H2V5zm2 2v.5l8 5.5 8-5.5V7H4z"/></svg><span>youremail@brantwellinc.example</span></li>
    </ul>
    <p class="website--front">www.brantwellinc.example</p>
  </section>

  <section class="card card--back" aria-label="Business card back">
    <div class="wordmark--back"><span class="wordmark__square"></span>Brantwell Construction Inc.</div>
    <p class="website--back">www.brantwellinc.example</p>
    <p class="services">Site development <span>|</span> Highway <span>|</span> Environmental <span>|</span> Demolition <span>|</span> Utility <span>|</span> Aggregate</p>
  </section>
</body>
</html>
```